New Webpage for High Class Expert Witness Services Company

We are looking for a minimalist design for a webpage that just has our logo and an entry form offer to connect with one of our Liaisons.
The entry form should just ask for Name, Email, Contact Info and Description of Project.

Company Name is: The Marlow Crest Advisory Services

Number of Pages Required

1 page

```html
<!DOCTYPE html>
<html lang="en">
<head>
<meta charset="utf-8">
<title>The Marlow Crest Advisory Services – Contact</title>
<link rel="stylesheet" href="https://fonts.googleapis.com/css2?family=Cinzel:wght@600&family=Poppins:wght@400;500;600;700&display=swap">
<style>
:root{
  --brand-red:#9e1b2c;
  --ink:#2b2f36;
  --muted:#5a5f66;
  --hero-top:#e4f2fd;
  --hero-bottom:#cfe6f6;
  --card:rgba(255,255,255,.6);
  --field:#ffffff;
}
*{box-sizing:border-box;margin:0;padding:0}
html,body{width:1091px;height:1200px;overflow:hidden;background:#fff;font-family:"Poppins",sans-serif;color:var(--ink)}
.page{position:relative;width:1091px;height:1200px}

.site-header{position:absolute;left:0;top:0;width:100%;height:73px;border-bottom:2px dashed #c9d6e2}
.brand{position:absolute;left:109px;top:24px;display:flex;align-items:center;gap:8px;font-weight:600;font-size:14px;letter-spacing:.5px;color:var(--ink)}
.brand-dot{width:14px;height:14px;background:var(--brand-red)}
.header-call{position:absolute;left:810px;top:18px;width:172px;height:36px;background:var(--brand-red);color:#fff;display:flex;align-items:center;justify-content:center;gap:8px;font-weight:500;font-size:14px;letter-spacing:.5px}

.hero{position:absolute;left:0;top:74px;width:100%;height:726px;overflow:hidden}
.hero-scene{position:absolute;inset:0;background:linear-gradient(180deg,var(--hero-top) 0%,var(--hero-bottom) 100%)}
.hero-title{position:absolute;top:50px;width:100%;text-align:center;font-family:"Cinzel",serif;font-weight:600;font-size:35px;color:var(--ink);letter-spacing:.5px}
.hero-sub{position:absolute;top:96px;width:100%;text-align:center;font-size:16px;color:var(--muted);letter-spacing:.6px}

.contact-card{position:absolute;left:218px;top:149px;width:655px;height:508px;border-radius:24px;background:var(--card);border:2px solid rgba(255,255,255,.9)}
.card-title{position:absolute;top:40px;width:100%;text-align:center;font-size:18px;font-weight:400;letter-spacing:.8px;color:var(--ink)}
.field{position:absolute;left:72px;width:509px;height:44px;border-radius:22px;background:var(--field);box-shadow:0 2px 4px rgba(0,0,0,.08);padding:13px 0 0 33px;font-size:12px;font-weight:500;letter-spacing:.5px;color:var(--ink)}
.field .req{color:var(--brand-red)}
.field-name{top:83px}
.field-email{top:138px}
.field-phone{top:192px}
.field-desc{top:247px;height:145px;border-radius:24px;padding-top:16px}
.submit{position:absolute;left:229px;top:418px;width:197px;height:43px;background:var(--brand-red);color:#fff;font-weight:600;font-size:14px;letter-spacing:.8px;display:flex;align-items:center;justify-content:center}

.hero-rule{position:absolute;left:0;top:799px;width:100%;border-top:2px dashed var(--brand-red)}

.footer-brand{position:absolute;left:109px;top:878px;display:flex;align-items:center;gap:10px;font-weight:600;font-size:22px;letter-spacing:.8px;color:var(--ink)}
.footer-brand .brand-dot{width:20px;height:20px}
.copyright{position:absolute;left:109px;top:938px;font-size:12px;line-height:20px;color:var(--ink)}
.socials{position:absolute;left:109px;top:1002px;display:flex;gap:14px}
.socials span{width:13px;height:13px;border-radius:50%;background:var(--ink);display:block}

.col-title{position:absolute;top:877px;font-weight:700;font-size:14px;letter-spacing:.5px;color:var(--ink)}
.sitemap{position:absolute;left:438px;top:920px;list-style:none;font-size:12px;letter-spacing:.4px}
.sitemap li{height:29px}
.chev{display:inline-block;width:5px;height:5px;border-right:1.3px solid var(--ink);border-bottom:1.3px solid var(--ink);transform:rotate(45deg);margin:0 0 3px 5px}

.icon-badge{position:absolute;width:29px;height:29px;border-radius:50%;background:var(--brand-red);display:flex;align-items:center;justify-content:center}
.info{position:absolute;font-size:10.5px;line-height:15px;letter-spacing:.2px;color:var(--ink)}
</style>
</head>
<body>
<div class="page">

  <header class="site-header">
    <div class="brand"><span class="brand-dot"></span>MARLOW CREST ADVISORY SERVICES</div>
    <div class="header-call">
      <svg width="13" height="13" viewBox="0 0 24 24"><path fill="#fff" d="M6.6 10.8a15.2 15.2 0 0 0 6.6 6.6l2.2-2.2a1 1 0 0 1 1-.25 11.4 11.4 0 0 0 3.6.57 1 1 0 0 1 1 1V20a1 1 0 0 1-1 1A17 17 0 0 1 3 4a1 1 0 0 1 1-1h3.5a1 1 0 0 1 1 1c0 1.25.2 2.45.57 3.57a1 1 0 0 1-.25 1z"/></svg>
      (310) 555-0142
    </div>
  </header>

  <section class="hero">
    <div class="hero-scene" role="img" aria-label="Background photo of a coastline and a suspension bridge"></div>
    <h1 class="hero-title">DEFENSE SERVICES</h1>
    <p class="hero-sub">Contact our Defense Liaisons</p>

    <form class="contact-card">
      <h2 class="card-title">Connect With Us</h2>
      <div class="field field-name">Name<span class="req">*</span></div>
      <div class="field field-email">Email<span class="req">*</span></div>
      <div class="field field-phone">Contact number<span class="req">*</span></div>
      <div class="field field-desc">Description of Project...</div>
      <div class="submit">SUBMIT</div>
    </form>
  </section>
  <div class="hero-rule"></div>

  <footer>
    <div class="footer-brand"><span class="brand-dot"></span>MARLOW CREST</div>
    <p class="copyright">Copyright © 2026 The Marlow Crest<br>All Rights Reserved.</p>
    <div class="socials" aria-label="Social links"><span></span><span></span><span></span><span></span><span></span></div>

    <h3 class="col-title" style="left:438px">SITE MAP</h3>
    <ul class="sitemap">
      <li>Stakeholders</li>
      <li>Physicians</li>
      <li>Services<span class="chev"></span></li>
      <li>Education<span class="chev"></span></li>
      <li>News</li>
      <li>Contact Us</li>
    </ul>

    <h3 class="col-title" style="left:628px">CONTACT INFO</h3>
    <div class="icon-badge" style="left:628px;top:920px">
      <svg width="11" height="13" viewBox="0 0 24 28"><path fill="#fff" d="M12 0a10 10 0 0 0-10 10c0 7.5 10 18 10 18s10-10.5 10-18A10 10 0 0 0 12 0zm0 14a4 4 0 1 1 0-8 4 4 0 0 1 0 8z"/></svg>
    </div>
    <p class="info" style="left:663px;top:921px">48 Harbor Row / 3rd Floor /<br>San Francisco, CA 94105</p>
    <p class="info" style="left:663px;top:966px">712 Orchard Ln / Ste 110 /<br>Santa Ana, CA 92704</p>

    <div class="icon-badge" style="left:869px;top:920px">
      <svg width="12" height="12" viewBox="0 0 24 24"><path fill="#fff" d="M6.6 10.8a15.2 15.2 0 0 0 6.6 6.6l2.2-2.2a1 1 0 0 1 1-.25 11.4 11.4 0 0 0 3.6.57 1 1 0 0 1 1 1V20a1 1 0 0 1-1 1A17 17 0 0 1 3 4a1 1 0 0 1 1-1h3.5a1 1 0 0 1 1 1c0 1.25.2 2.45.57 3.57a1 1 0 0 1-.25 1z"/></svg>
    </div>
    <p class="info" style="left:905px;top:926px">(800) 555-0176</p>
    <div class="icon-badge" style="left:869px;top:961px">
      <svg width="12" height="12" viewBox="0 0 24 24"><path fill="#fff" d="M3 9c5-5 13-5 18 0l-2 3-3-1V9a8 8 0 0 0-8 0v2l-3 1zM6 14h12l1 6H5zm4 2v2h4v-2z"/></svg>
    </div>
    <p class="info" style="left:905px;top:967px">(310) 555-0142</p>
  </footer>

</div>
</body>
</html>
```